Business card for Delacroft Anesthesia LLC

This is for a business care for Delacroft Anesthesia LLC. Dr. Helen Delacroft, CRNA, DNAP is the sole provider in the LLC. Business address is 4716 N Brackley Avenue,
Furlong, PA 18925
CRNA stands for certified registered nurse anesthetist
"Keeping you safe and comfortable"
I plan to give this business card to the patients that I provide anesthesia to.
Creative design that ties into Anesthesia. Calm soothing colors.

Target Market(s)

Business card for my patients.

Industry/Entity Type

Medicine

Contact Information for Business Card

Creative, professional, eye catching

Logo Text

Delacroft Anesthesia

Font styles to use
Serif
Script

Colors

Designer to choose colors to be used in the design.

Requirements
Must have
• Delacroft Anesthesia
• Dr. Helen Delacroft, CRNA, DNAP
• delacroft.anesthesia@ quillmail.net
Nice to have
• "Keeping you safe and comfortable"
Should not have
• phone number

```html
<!DOCTYPE html>
<html lang="en">
<head>
<meta charset="utf-8">
<title>Delacroft Anesthesia – Business Card</title>
<link rel="stylesheet" href="https://fonts.googleapis.com/css2?family=Varela+Round&display=swap">
<style>
  :root {
    --stage: #000000;
    --teal: #0aa58b;
    --blue: #0a84c6;
    --card-white: #ffffff;
    --grey-text: #6b6b6b;
    --green-rule: #14a88a;
  }
  * { margin: 0; padding: 0; box-sizing: border-box; }
  html, body {
    width: 1200px; height: 1000px; overflow: hidden;
    background: var(--stage);
    font-family: "Varela Round", sans-serif;
  }
  .canvas { position: relative; width: 1200px; height: 1000px; }
  .card {
    position: absolute; left: 258px; width: 682px; height: 388px;
    border-radius: 40px; overflow: hidden;
  }
  .card--front {
    top: 83px;
    background: linear-gradient(180deg, var(--teal) 0%, #0a96a8 50%, var(--blue) 100%);
  }
  .card--back { top: 520px; background: var(--card-white); }

  .front-emblem {
    position: absolute; left: 311px; top: 110px; width: 60px; height: 60px;
    border: 3px solid rgba(255,255,255,0.9); border-radius: 50%;
  }
  .front-name {
    position: absolute; left: 0; right: 0; top: 200px; text-align: center;
    color: #fff; font-size: 34px; line-height: 40px;
  }
  .front-tagline {
    position: absolute; left: 0; right: 0; top: 245px; text-align: center;
    color: #fff; font-size: 15px; letter-spacing: 1px;
  }

  .back-emblem {
    position: absolute; left: 186px; top: 52px; width: 58px; height: 58px;
    border: 3px solid var(--blue); border-radius: 50%;
  }
  .back-name {
    position: absolute; left: 50px; top: 127px;
    color: var(--blue); font-size: 30px; line-height: 38px;
  }
  .back-tagline {
    position: absolute; left: 51px; top: 164px;
    color: var(--grey-text); font-size: 13.5px; letter-spacing: 0.6px;
  }
  .holder-name {
    position: absolute; right: 47px; top: 236px;
    color: var(--blue); font-size: 26px; line-height: 32px;
  }
  .holder-dash {
    position: absolute; left: 644px; top: 255px; width: 26px; height: 4px;
    background: var(--green-rule);
  }
  .holder-rule {
    position: absolute; left: 14px; top: 286px; width: 477px; height: 4px;
    background: var(--green-rule);
  }
  .holder-credentials {
    position: absolute; right: 47px; top: 276px;
    color: var(--green-rule); font-size: 20px; line-height: 26px;
  }
  .contact-email {
    position: absolute; right: 79px; top: 327px;
    color: var(--grey-text); font-size: 22px; line-height: 28px;
  }
  .contact-icon { position: absolute; left: 614px; top: 324px; width: 36px; height: 36px; }
</style>
</head>
<body>
<main class="canvas">
  <section class="card card--front" role="img" aria-label="Teal to blue gradient card face with a faint repeating brand pattern">
    <div class="front-emblem"></div>
    <p class="front-name">Delacroft Anesthesia</p>
    <p class="front-tagline">KEEPING YOU SAFE AND COMFORTABLE</p>
  </section>

  <section class="card card--back">
    <div class="back-emblem"></div>
    <p class="back-name">Delacroft Anesthesia</p>
    <p class="back-tagline">KEEPING YOU SAFE AND COMFORTABLE</p>

    <p class="holder-name">Dr. Helen Delacroft</p>
    <span class="holder-dash"></span>
    <span class="holder-rule"></span>
    <p class="holder-credentials">CRNA, DNAP</p>

    <p class="contact-email">delacroft.anesthesia@quillmail.net</p>
    <svg class="contact-icon" viewBox="0 0 36 36" aria-hidden="true">
      <circle cx="18" cy="18" r="16" fill="none" stroke="#0a84c6" stroke-width="2.5"/>
      <rect x="10" y="12" width="16" height="12" rx="1.5" fill="#0a84c6"/>
      <polyline points="10.5,12.8 18,19 25.5,12.8" fill="none" stroke="#fff" stroke-width="1.6"/>
    </svg>
  </section>
</main>
</body>
</html>
```